Corporate Design Glasanlagen
Zielgruppe
Individuelle Fertigung von Glasanlagen (Duschabtrennungen, Glasrückwände, Glastüren, Glastrennwände, Spiegel, Lichtspiegel, Spiegelschränke, Ablagen, Waschtische, Digitaldruck)
Individuelle Anfertigung von Möbeln (Badmöbel, Sideboards, Schränke, Regale, Plattenlösungen)
Aufgabenstellung
Ein passender Slogan kann muss aber nicht hinzugefügt werden,
Klares Design, 1 - 2 Farben, Grautöne sind zusätzlich möglich,
Keine Rottöne,
zusätzliche Infos:
Holzoptik möglich (im Logo oder als Hintergrund)
im Würmtal liegt der naturbelassener Bach, die Würm
Logo oberhalb des Schriftzuges

```html
<!DOCTYPE html>
<html lang="de">
<head>
<meta charset="utf-8">
<title>Lindtal Werkstatt – Visitenkarte</title>
<link rel="stylesheet" href="https://fonts.googleapis.com/css2?family=Open+Sans:wght@800&family=Fira+Sans:wght@400&display=swap">
<style>
  :root {
    --page: #ffffff;
    --card: #f2f2f4;
    --ink: #666b72;
    --gold: #c49a6c;
  }
  * { margin: 0; padding: 0; box-sizing: border-box; }
  html, body {
    width: 1200px;
    height: 706px;
    overflow: hidden;
    background: var(--page);
  }
  .sheet {
    position: relative;
    width: 1200px;
    height: 706px;
  }
  .card {
    position: absolute;
    top: 173px;
    width: 538px;
    height: 333px;
    background: var(--card);
  }
  .card--front { left: 42px; }
  .card--back { left: 615px; }

  .brand {
    position: absolute;
    display: flex;
    flex-direction: column;
    align-items: center;
    font-family: "Open Sans", Arial, sans-serif;
    font-weight: 800;
    color: var(--ink);
    white-space: nowrap;
  }
  .brand__square {
    display: block;
    background: var(--gold);
  }
  .brand__name { display: block; line-height: 1; }

  .card--front .brand {
    left: 10px;
    width: 300px;
    top: 104px;
    gap: 24px;
    font-size: 20px;
    letter-spacing: 1.2px;
  }
  .card--front .brand__square { width: 72px; height: 72px; }

  .card--back .brand {
    left: 119px;
    width: 300px;
    top: 90px;
    gap: 30px;
    font-size: 24px;
    letter-spacing: 1.4px;
  }
  .card--back .brand__square { width: 90px; height: 90px; }

  .divider {
    position: absolute;
    left: 300px;
    top: 84px;
    width: 1px;
    height: 163px;
    background: var(--ink);
  }
  .contact {
    position: absolute;
    left: 327px;
    top: 96px;
    font-family: "Fira Sans", Arial, sans-serif;
    font-weight: 400;
    color: var(--ink);
    font-size: 13px;
    letter-spacing: 1px;
    line-height: 19px;
    list-style: none;
  }
  .contact__phone { letter-spacing: 0.8px; }
  .contact__address { margin-top: 10px; }
  .contact__email { margin-top: 17px; }
  .contact__web { margin-top: 4px; letter-spacing: 1.6px; }
</style>
</head>
<body>
  <main class="sheet">
    <section class="card card--front" aria-label="Vorderseite">
      <div class="brand">
        <span class="brand__square" aria-hidden="true"></span>
        <span class="brand__name">Lindtal Werkstatt</span>
      </div>
      <div class="divider" aria-hidden="true"></div>
      <ul class="contact">
        <li class="contact__phone">123 - 456789</li>
        <li class="contact__phone">123 - 456789</li>
        <li class="contact__address">YOUR ADRESS GOES HERE<br>YOUR ADRESS GOES HERE</li>
        <li class="contact__email">YOURWEB@EMAIL.COM</li>
        <li class="contact__web">WWW.WEBSITE.COM</li>
      </ul>
    </section>

    <section class="card card--back" aria-label="Rückseite">
      <div class="brand">
        <span class="brand__square" aria-hidden="true"></span>
        <span class="brand__name">Lindtal Werkstatt</span>
      </div>
    </section>
  </main>
</body>
</html>
```